Silver Kettle Consulting

I need a business card design and for my consulting business. I provide outsourced CFO services for start-ups and high growth companies. I call my company Silver Kettle because building a company is similar to building a stone pathway, selecting each stone and planning several stones head in order to properly place them - all while keeping an eye on the final design and curve of the path. The underlying idea I want to express with my marketing images is that I'm someone that you can count on to help build your business and be there step by step to help. I'm not the old gray-haired CFO that many folks think of. :) I've included a one-page summery that I'm working on, it includes a summary of what I do. I've used a muted pathway and with greens in the header , and do like the green, but am open to other colors if they work well. Would like something that looks like a pathway, but a more abstract version instead of a picture.

Marketing

```html
<!DOCTYPE html>
<html lang="en">
<head>
<meta charset="utf-8">
<title>Silver Kettle Consulting – Business Card</title>
<link rel="stylesheet" href="https://fonts.googleapis.com/css2?family=Ubuntu:wght@400;500&display=swap">
<style>
  :root {
    --backdrop: #d6d6d3;
    --green-light: #8cc9a4;
    --green-mid: #2a9a62;
    --green-deep: #13874f;
    --rule: #eef2ef;
    --ink: #111a15;
    --ink-soft: #1d2a22;
    --tint: #d3ecdc;
    --white: #ffffff;
  }
  * { box-sizing: border-box; margin: 0; padding: 0; }
  html, body {
    width: 1200px; height: 1000px; overflow: hidden;
    background: var(--backdrop);
    font-family: "Ubuntu", sans-serif;
  }
  .card {
    position: absolute; left: 220px;
    width: 760px; height: 434px;
    overflow: hidden;
    box-shadow: 0 4px 14px rgba(0,0,0,0.18);
  }
  .card--front { top: 40px; }
  .card--back  { top: 526px; }

  .card__field {
    position: absolute; left: 0; right: 0; top: 0;
    background: linear-gradient(to bottom, var(--green-light) 0%, var(--green-mid) 70%, var(--green-deep) 100%);
  }
  .card__rule {
    position: absolute; left: 0; right: 0; height: 7px;
    background: var(--rule);
  }
  .card__band {
    position: absolute; left: 0; right: 0; bottom: 0;
    background: var(--green-deep);
  }

  /* Front */
  .card--front .card__field { height: 236px; }
  .card--front .card__rule  { top: 236px; }
  .card--front .card__band  { top: 243px; }
  .brand { position: absolute; text-align: right; color: var(--ink); }
  .brand__name { font-weight: 500; letter-spacing: 0.04em; line-height: 1; }
  .brand__tag  { font-weight: 400; line-height: 1.2; }
  .card--front .brand { right: 46px; top: 70px; }
  .card--front .brand__name { font-size: 58px; }
  .card--front .brand__tag  { font-size: 24px; margin-top: 16px; color: var(--ink-soft); }
  .tagline {
    position: absolute; left: 120px; right: 40px; top: 262px;
    color: var(--tint); font-size: 19px; line-height: 1.3;
  }

  /* Back */
  .card--back .card__field { height: 186px; }
  .card--back .card__rule  { top: 186px; }
  .card--back .card__band  { top: 193px; }
  .person { position: absolute; left: 50px; top: 66px; color: var(--ink); }
  .person__name  { font-size: 30px; font-weight: 400; }
  .person__title { font-size: 24px; font-weight: 400; margin-top: 18px; margin-left: -22px; }
  .card--back .brand { right: 40px; top: 64px; }
  .card--back .brand__name { font-size: 27px; }
  .card--back .brand__tag  { font-size: 14px; margin-top: 6px; color: var(--ink-soft); }

  .contact {
    position: absolute; display: flex; align-items: center; gap: 18px;
    color: var(--tint); font-size: 24px; letter-spacing: 0.03em;
  }
  .contact--phone { left: 80px; top: 268px; }
  .contact--email { right: 40px; top: 350px; color: var(--white); font-size: 26px; }
  .contact__icon { flex: none; }
</style>
</head>
<body>

<section class="card card--front" aria-label="Card front">
  <div class="card__field"></div>
  <div class="card__rule"></div>
  <div class="card__band"></div>
  <div class="brand">
    <div class="brand__name">Silver Kettle</div>
    <div class="brand__tag">Consulting Services</div>
  </div>
  <p class="tagline">Exclusive Finance and Operations Expertise on a Part-time,<br>Ongoing Engagement or Project Basis</p>
</section>

<section class="card card--back" aria-label="Card back">
  <div class="card__field"></div>
  <div class="card__rule"></div>
  <div class="card__band"></div>
  <div class="person">
    <div class="person__name">Dana Whitfield, CPA</div>
    <div class="person__title">Consultant</div>
  </div>
  <div class="brand">
    <div class="brand__name">Silver Kettle</div>
    <div class="brand__tag">Consulting Services</div>
  </div>
  <div class="contact contact--phone">
    <svg class="contact__icon" width="22" height="36" viewBox="0 0 22 36" aria-hidden="true">
      <rect x="1.5" y="1.5" width="19" height="33" rx="3" fill="none" stroke="#d3ecdc" stroke-width="2"/>
      <line x1="1.5" y1="6.5" x2="20.5" y2="6.5" stroke="#d3ecdc" stroke-width="1.5"/>
      <line x1="1.5" y1="28.5" x2="20.5" y2="28.5" stroke="#d3ecdc" stroke-width="1.5"/>
    </svg>
    <span>555-014-2286</span>
  </div>
  <div class="contact contact--email">
    <svg class="contact__icon" width="38" height="26" viewBox="0 0 38 26" aria-hidden="true">
      <rect x="1" y="1" width="36" height="24" fill="#ffffff"/>
      <polyline points="1,1 19,15 37,1" fill="none" stroke="#13874f" stroke-width="2"/>
      <polyline points="1,25 14,11 M37,25 24,11" fill="none" stroke="#13874f" stroke-width="1.5"/>
      <line x1="1" y1="25" x2="14" y2="11" stroke="#13874f" stroke-width="1.5"/>
      <line x1="37" y1="25" x2="24" y2="11" stroke="#13874f" stroke-width="1.5"/>
    </svg>
    <span>dana@silverkettle.com</span>
  </div>
</section>

</body>
</html>
```